Business Card Design Project

We need a business card design for a consultancy called 'Amber Ridge'. The design should communicate innovation and professionalism. The colors used should complement our logo. Please include source files for winning design.
Updates

Industry/Entity Type

Business

Colors

Designer to choose colors to be used in the design.

Requirements
Must have
• Card size should be 85mm x 50mm. The back side of the card should be the logo on a black background. The front side should display the name 'Amber Ridge' along with standard information. The front's design should graphically complement the back.
Nice to have
• Any graphical elements in the front the complement the back side (with the logo on a black background) would be a plus.

```html
<!DOCTYPE html>
<html lang="en">
<head>
<meta charset="utf-8">
<title>Amber Ridge – Business Card</title>
<link rel="stylesheet" href="https://fonts.googleapis.com/css2?family=Cinzel:wght@600&family=Exo+2:wght@400;500;600&display=swap">
<style>
  :root {
    --page: #e9e7e3;
    --card-white: #f4f4f4;
    --card-black: #0b0b0b;
    --amber: #f39a2b;
    --ink: #2b2b2b;
    --white: #ffffff;
  }
  * { margin: 0; padding: 0; box-sizing: border-box; }
  html, body { width: 1200px; height: 1085px; overflow: hidden; }
  body {
    background: var(--page);
    display: flex; align-items: center; justify-content: center;
    font-family: "Exo 2", sans-serif;
  }
  .card {
    position: relative; width: 1000px; height: 588px;
    background: var(--card-white);
    box-shadow: 0 10px 30px rgba(0,0,0,.18);
    overflow: hidden;
  }
  .card-shape { position: absolute; inset: 0; }
  .contact-row {
    position: absolute; right: 490px;
    text-align: right; color: var(--ink);
    font-size: 27px; font-weight: 500; line-height: 1.3; letter-spacing: .5px;
    transform: translateY(-50%);
  }
  .row-phone { top: 150px; }
  .row-address { top: 294px; }
  .row-web { top: 438px; }
  .brand-mark {
    position: absolute; left: 720px; top: 62px;
    width: 170px; height: 170px; border-radius: 50%;
    background: var(--amber);
    border: 6px solid var(--card-black);
    box-shadow: 0 0 0 4px var(--amber);
  }
  .brand-name {
    position: absolute; left: 640px; width: 330px; top: 268px;
    text-align: center;
    font-family: "Cinzel", serif; font-weight: 600;
    font-size: 42px; color: var(--amber); letter-spacing: 1px;
  }
  .person { position: absolute; left: 640px; width: 330px; top: 360px; text-align: center; color: var(--white); }
  .person-name { font-size: 32px; font-weight: 600; letter-spacing: 1.5px; }
  .person-title { font-size: 23px; font-weight: 400; margin-top: 4px; }
</style>
</head>
<body>
  <div class="card">
    <svg class="card-shape" width="1000" height="588" viewBox="0 0 1000 588">
      <path fill="var(--card-black)" d="M585 0 L585 90 C585 120 630 120 630 150 C630 180 585 180 585 210 L585 234 C585 264 630 264 630 294 C630 324 585 324 585 354 L585 378 C585 408 630 408 630 438 C630 468 585 468 585 498 L585 588 L1000 588 L1000 0 Z"/>
      <g fill="none" stroke="var(--amber)" stroke-width="4" stroke-linecap="round" stroke-linejoin="round">
        <circle cx="578" cy="150" r="25"/>
        <path d="M568 138 q-4 4 0 12 q6 12 18 16 q6 1 8 -3 l-5 -5 l-5 3 q-6 -3 -9 -10 l3 -5 z" stroke-width="3"/>
        <circle cx="578" cy="294" r="25"/>
        <path d="M578 309 c-8 -9 -11 -14 -11 -19 a11 11 0 0 1 22 0 c0 5 -3 10 -11 19 z" stroke-width="3"/>
        <circle cx="578" cy="289" r="3.5" stroke-width="2.5"/>
        <circle cx="578" cy="438" r="25"/>
        <g stroke-width="2.5">
          <circle cx="578" cy="438" r="13"/>
          <ellipse cx="578" cy="438" rx="6" ry="13"/>
          <path d="M565 438 h26 M567 431 h22 M567 445 h22"/>
        </g>
      </g>
    </svg>

    <div class="contact-row row-phone">014 728 3560<br>014 728 3561</div>
    <div class="contact-row row-address">27, 9th floor,<br>Harbour View Road<br>NKT</div>
    <div class="contact-row row-web">hello@amberridge.com<br>www.amberridge.com</div>

    <div class="brand-mark" aria-hidden="true"></div>
    <div class="brand-name">Amber Ridge</div>
    <div class="person">
      <div class="person-name">DANIEL MERCER</div>
      <div class="person-title">Managing Director</div>
    </div>
  </div>
</body>
</html>
```